Business Card and Stationary for Electrical Contractor
Vantor Electric
Business Card and Stationary for Electrical Contractor - Construction
Creative Brief
Professional
Dalton Pryce
Service Technician
1875 Birchwood Lane Kansas City, KS 66109
dpryce@vantorelectricmo.com
www.vantorelectricmo.com

```html
<!DOCTYPE html>
<html lang="en">
<head>
<meta charset="utf-8">
<title>Vantor Electric – Business Card</title>
<link href="https://fonts.googleapis.com/css2?family=Roboto:wght@400;500;700;900&display=swap" rel="stylesheet">
<style>
  :root {
    --bg: #e4e4e4;
    --white: #ffffff;
    --black: #0d0d0d;
    --red: #e3161f;
    --maroon: #5a1414;
    --grey-text: #222222;
  }
  * { margin: 0; padding: 0; box-sizing: border-box; }
  html, body {
    width: 1200px; height: 876px; overflow: hidden;
    background: var(--bg);
    font-family: "Roboto", Arial, sans-serif;
  }
  .card {
    position: absolute; left: 285px;
    width: 630px; height: 366px;
    background: var(--white); overflow: hidden;
  }
  .card--front { top: 40px; }
  .card--back { top: 470px; }
  .card-shapes { position: absolute; inset: 0; width: 630px; height: 366px; }

  .wordmark {
    position: absolute; color: var(--maroon);
    font-weight: 900; text-transform: uppercase; text-align: center;
    line-height: 1;
  }
  .wordmark-square {
    display: block; background: var(--maroon); margin: 0 auto;
  }
  .card--front .wordmark { left: 250px; top: 85px; width: 340px; font-size: 46px; letter-spacing: 4px; }
  .card--front .wordmark small { display: block; font-size: 20px; letter-spacing: 12px; margin-top: 10px; }
  .card--front .wordmark-square { width: 34px; height: 34px; margin-bottom: 14px; }

  .card--back .wordmark { left: 10px; top: 26px; width: 230px; font-size: 32px; letter-spacing: 3px; }
  .card--back .wordmark small { display: block; font-size: 14px; letter-spacing: 8px; margin-top: 6px; }
  .card--back .wordmark-square { width: 26px; height: 26px; margin-bottom: 10px; }

  .holder { position: absolute; left: 300px; top: 30px; width: 300px; }
  .holder-name { font-size: 36px; color: var(--black); letter-spacing: 1px; line-height: 1; text-transform: uppercase; }
  .holder-name b { font-weight: 700; }
  .holder-name span { font-weight: 400; }
  .holder-title {
    font-size: 15px; color: var(--red); font-weight: 500;
    border-bottom: 3px solid var(--red); padding-bottom: 2px; margin-top: 2px;
  }

  .contact-list { position: absolute; left: 245px; top: 178px; list-style: none; color: var(--white); }
  .contact-item { display: flex; align-items: center; font-size: 16px; font-weight: 700; margin-bottom: 14px; line-height: 1.15; }
  .contact-item svg { width: 20px; height: 20px; flex: none; margin-right: 22px; }
</style>
</head>
<body>

<section class="card card--front" aria-label="Business card front">
  <svg class="card-shapes" viewBox="0 0 630 366" aria-hidden="true">
    <defs>
      <linearGradient id="frontBandFade" x1="0" x2="1" y1="0" y2="0">
        <stop offset="0.45" stop-color="#e3161f"/>
        <stop offset="1" stop-color="#0d0d0d"/>
      </linearGradient>
    </defs>
    <rect width="630" height="366" fill="#0d0d0d"/>
    <polygon points="20,0 70,0 205,262 630,262 630,305 180,305" fill="url(#frontBandFade)"/>
    <polygon points="70,0 630,0 630,262 205,262" fill="#ffffff"/>
  </svg>
  <div class="wordmark">
    <span class="wordmark-square"></span>Vantor<small>Electric</small>
  </div>
</section>

<section class="card card--back" aria-label="Business card back">
  <svg class="card-shapes" viewBox="0 0 630 366" aria-hidden="true">
    <defs>
      <linearGradient id="backBandFade" x1="0" x2="1" y1="0" y2="0">
        <stop offset="0" stop-color="#ffffff"/>
        <stop offset="0.5" stop-color="#e3161f"/>
      </linearGradient>
    </defs>
    <polygon points="0,270 40,270 230,366 0,366" fill="url(#backBandFade)"/>
    <polygon points="150,165 190,165 290,366 250,366" fill="#e3161f"/>
    <polygon points="195,165 630,165 630,366 295,366" fill="#0d0d0d"/>
  </svg>

  <div class="wordmark">
    <span class="wordmark-square"></span>Vantor<small>Electric</small>
  </div>

  <div class="holder">
    <h1 class="holder-name"><b>Dalton</b> <span>Pryce</span></h1>
    <p class="holder-title">Service Technician</p>
  </div>

  <ul class="contact-list">
    <li class="contact-item">
      <svg viewBox="0 0 20 20" aria-hidden="true"><path d="M10 1a6 6 0 0 0-6 6c0 4.5 6 12 6 12s6-7.5 6-12a6 6 0 0 0-6-6zm0 8.5A2.5 2.5 0 1 1 10 4.5a2.5 2.5 0 0 1 0 5z" fill="#fff"/></svg>
      <span>1875 Birchwood Lane<br>Kansas City, KS 66109</span>
    </li>
    <li class="contact-item">
      <svg viewBox="0 0 20 20" aria-hidden="true"><path d="M5 2l3 4-2 2c1 2.5 3.5 5 6 6l2-2 4 3-2 3C9 18 2 11 2 4z" fill="#fff"/></svg>
      <span>913-555-0172, 816-555-0148</span>
    </li>
    <li class="contact-item">
      <svg viewBox="0 0 20 20" aria-hidden="true"><rect x="2" y="4" width="16" height="12" fill="#fff"/><path d="M2 4l8 7 8-7" fill="none" stroke="#0d0d0d" stroke-width="1.5"/></svg>
      <span>dpryce@vantorelectricmo.com</span>
    </li>
    <li class="contact-item">
      <svg viewBox="0 0 20 20" aria-hidden="true"><path d="M4 2l12 8-5 1 3 6-2 1-3-6-4 4z" fill="#fff"/></svg>
      <span>www.vantorelectricmo.com</span>
    </li>
  </ul>
</section>

</body>
</html>
```